Engineering Land Development Company Needs Flyer Brochure for Prospective Professional Clients

Our company provides land development site design for commercial projects. We have many repeat clients that are familiar with our work. We do not advertise our services other than a website. Most of our referrals are from existing clients. When a new client contacts us and asks for a proposal for a project we would like to have a brochure that shows our strengths, experience, and professionalism. We are selling professional services similar to a lawyer or accountant. We want new clients to feel comfortable hiring a new firm. The brochure would be one page single-side included when we submit proposals for new projects. Check out our website at tovamrk.net for more info. We would like a brochure that mixes grading/excavation construction work on a job site with business professional. We will need to update the brochure so we want it in .doc .psd or some other edit format. The brochure we are using is attached. It is very two-dimensional. We need some depth.

Target Market(s)

Land developers, architects, real estate, professionals, attorneys

Industry/Entity Type

Real Estate Development

Font styles to use
Sans Serif
Other font styles liked:
• calibri

Colors
0355a3
9bcb3c

Requirements
Must have
• company logo, ability to update text and images
Nice to have
• background image(s) with text overlay
Should not have
• cartoons, harsh colors, stock photos of people, lots of boxes

```html
<!DOCTYPE html>
<html lang="en">
<head>
<meta charset="utf-8">
<title>Tovamark Engineering PLLC – Land Development Services</title>
<link rel="stylesheet" href="https://fonts.googleapis.com/css2?family=Source+Sans+3:ital,wght@0,400;0,600;0,700;1,400&family=Source+Serif+4:wght@300;400&display=swap">
<style>
  :root {
    --violet: #6a6af2;
    --green: #2cb54a;
    --ink: #2b2b2b;
    --muted: #3a3a3a;
    --page: #ffffff;
    --stage: #ececec;
  }
  html, body {
    margin: 0; width: 1200px; height: 1200px; overflow: hidden;
    background: var(--stage);
  }
  .flyer {
    position: absolute; left: 151px; top: 18px;
    width: 820px; height: 1060px;
    transform: scale(1.097); transform-origin: top left;
    background: linear-gradient(180deg, #ffffff 0%, #f4f4f4 60%, #f7f7f7 100%);
    overflow: hidden;
    font-family: "Source Sans 3", "Calibri", sans-serif;
    color: var(--ink);
    box-shadow: 0 6px 18px rgba(0,0,0,.18);
  }
  .art { position: absolute; left: 0; top: 0; }
  .brand {
    position: absolute; left: 50px; top: 198px;
    display: flex; align-items: center; gap: 8px;
  }
  .brand-square { width: 30px; height: 30px; background: var(--violet); }
  .brand-name {
    font-family: "Source Serif 4", serif; font-weight: 300;
    font-size: 27px; color: var(--violet); letter-spacing: -0.5px;
  }
  .brand-name small { font-family: "Source Sans 3", sans-serif; font-size: 19px; color: var(--green); font-weight: 400; margin-left: 4px; }
  .mission {
    position: absolute; left: 44px; top: 255px; width: 720px;
    margin: 0; font-size: 19px; line-height: 24px; font-weight: 600; color: var(--green);
  }
  .intro {
    position: absolute; left: 42px; top: 308px; width: 724px;
    margin: 0; font-size: 13.5px; line-height: 18px; font-style: italic; color: var(--muted);
  }
  .service { position: absolute; left: 0; width: 780px; }
  .service-label {
    position: absolute; left: 30px; width: 120px; text-align: center;
    font-size: 14px; font-style: italic; color: var(--violet); font-weight: 400; letter-spacing: .2px;
  }
  .service-photo {
    position: absolute; left: 42px; width: 84px; height: 84px; border-radius: 50%;
    border: 4px solid var(--green); box-sizing: border-box;
  }
  .service-title {
    position: absolute; left: 168px; width: 606px; margin: 0;
    font-size: 14px; line-height: 18px; font-weight: 600; color: var(--ink);
  }
  .service-text {
    position: absolute; left: 168px; width: 604px; margin: 0;
    font-size: 13.3px; line-height: 18px; font-style: italic; color: var(--muted); text-align: justify;
  }
  .clients-note {
    position: absolute; left: 31px; top: 926px; width: 230px; margin: 0;
    font-size: 13.5px; line-height: 18px; font-style: italic; color: var(--ink);
  }
  .client-row {
    position: absolute; left: 266px; width: 490px;
    display: flex; justify-content: space-between; align-items: center;
  }
  .client-row span { font-size: 9px; font-weight: 700; color: #555; width: 46px; text-align: center; }
  .footer {
    position: absolute; left: 0; top: 1011px; width: 820px; height: 49px;
    background: var(--violet); color: #fff;
    display: flex; align-items: center; justify-content: center;
    font-size: 13.5px; font-weight: 600;
  }
</style>
</head>
<body>
<div class="flyer">
  <svg class="art" width="820" height="1060" viewBox="0 0 820 1060">
    <defs>
      <linearGradient id="steelTone" x1="0" y1="0" x2="0" y2="1">
        <stop offset="0" stop-color="#9fb3c8"/><stop offset="1" stop-color="#6f6a62"/>
      </linearGradient>
      <linearGradient id="siteTone" x1="0" y1="0" x2="0" y2="1">
        <stop offset="0" stop-color="#4f8fe0"/><stop offset=".45" stop-color="#c9a34a"/><stop offset="1" stop-color="#d07a3e"/>
      </linearGradient>
    </defs>
    <path role="img" aria-label="Photo of a steel-frame building under construction"
      d="M0,0 H431 V168 C380,165 330,160 300,158 C210,150 150,160 130,118 C100,62 60,40 0,30 Z" fill="url(#steelTone)"/>
    <path role="img" aria-label="Photo of an excavator digging red clay on a job site"
      d="M441,0 H820 V185 C760,205 680,212 560,190 C510,180 475,174 441,170 Z" fill="url(#siteTone)"/>
    <path d="M0,30 C60,40 100,62 130,118 C150,160 210,150 300,158 C420,168 450,170 560,190 C680,212 760,205 820,185 V210 C760,228 680,232 560,212 C450,192 420,180 300,172 C200,166 150,175 122,128 C95,75 55,55 0,48 Z" fill="var(--violet)"/>
    <path d="M820,212 C800,240 790,320 792,420 C795,560 800,720 782,880 C776,950 772,990 770,1011 H820 Z" fill="var(--green)"/>
    <line x1="100" y1="381" x2="720" y2="381" stroke="#e2e2e2" stroke-width="1"/>
    <line x1="180" y1="895" x2="720" y2="895" stroke="#e2e2e2" stroke-width="1"/>
  </svg>

  <div class="brand">
    <div class="brand-square"></div>
    <div class="brand-name">Tovamark Engineering<small>PLLC</small></div>
  </div>

  <h1 class="mission">Our mission at Tovamark Engineering is to provide Superior Quality Professional Land Development Services</h1>
  <p class="intro">Our firm provides planning, surveying, engineering, and environmental services which allows us to focus on the entire land development process rather than one specific discipline. Providing a broad scope of professional services helps to streamline a project by eliminating many disadvantages of having multiple firms with overlapping responsibilities.</p>

  <section class="service">
    <div class="service-label" style="top:396px">PLANNING</div>
    <div class="service-photo" style="top:416px;background:#c9c56a" role="img" aria-label="Site plan map of subdivided lots"></div>
    <h2 class="service-title" style="top:398px">We are land development professionals who can see the “big picture”.</h2>
    <p class="service-text" style="top:426px">We have extensive experience with site selection, due diligence investigations, re-zonings, and land planning. Every project is different. We look forward to identifying all feasible alternatives. We become part of the project and enjoy developing the best plan for the success of each particular project. We understand that time is money and unexpected delays are unacceptable.</p>
  </section>

  <section class="service">
    <div class="service-label" style="top:522px">SURVEYING</div>
    <div class="service-photo" style="top:542px;background:linear-gradient(#2e4f9a,#d9b22a)" role="img" aria-label="Surveying total station instrument"></div>
    <h2 class="service-title" style="top:520px">We are land development professionals who provide superior quality surveying services.</h2>
    <p class="service-text" style="top:546px">Our firm can handle any surveying need. We have extensive experience with ALTA surveys, boundary surveys, subdivision platting, topographic/location surveys, GPS surveys, R/W surveys, construction staking, as-built surveys, elevation certificates, etc. We work closely with title attorneys to provide legal descriptions, exhibits, and other assistance when closing the real estate deal.</p>
  </section>

  <section class="service">
    <div class="service-label" style="top:646px">ENGINEERING</div>
    <div class="service-photo" style="top:671px;background:#e6e6e6" role="img" aria-label="Engineering site drawing of roads and utilities"></div>
    <h2 class="service-title" style="top:642px">We are land development professionals who can handle the most complicated engineering challenge.</h2>
    <p class="service-text" style="top:682px;line-height:17px">Let us worry about all the technical stuff and the regulators. Our firm has extensive experience with infrastructure assessments, erosion control, grading, roadway design, stormwater management, water systems, sewer systems, utilities, flood plain management, landscape design, permitting, bidding, and construction administration.</p>
  </section>

  <section class="service">
    <div class="service-label" style="top:780px">ENVIRONMENTAL</div>
    <div class="service-photo" style="top:800px;background:linear-gradient(#7fa14a,#4f6e2c)" role="img" aria-label="Wetland grasses"></div>
    <h2 class="service-title" style="top:779px">We are land development professionals who provide superior quality environmental services.</h2>
    <p class="service-text" style="top:807px;line-height:17px">We provide environmental site assessments, underground storage tank management, soil and groundwater sampling and testing, contamination remediation, Brownfields assessments, permitting and redevelopment, and wetlands permitting. Our firm works closely with state and federal agencies to provide economical mitigation and remediation solutions</p>
  </section>

  <p class="clients-note">Our business would not be successful without the support of our clients. Some of our project clients include:</p>
  <div class="client-row" style="top:926px">
    <span>Parkland</span><span>Quilla</span><span>Craftly</span><span>Panhouse</span><span>Morrow's</span><span>Pizzeria</span><span>AutoCo</span><span>Fieldco</span><span>Homeway</span><span>Kanto</span>
  </div>
  <div class="client-row" style="top:966px">
    <span>Telnet</span><span>Vala Foods</span><span>Burrito Co</span><span>Taqui</span><span>GrocerLn</span><span>Brewhaus</span><span>WingHub</span><span>Burgerly</span><span>PetPal</span>
  </div>

  <footer class="footer">410 Ridgeway Avenue – Suite 200, Ashford Falls, NC 28000 | Call: (555) 014-2700 | Visit: www.tovamrk.net</footer>
</div>
</body>
</html>
```